Online Media Company Website

Looking for a website design that clearly and powerfully portrays our brand. Vantorell. We are an online media technology company that helps advertisers understand the content and verify the context where they advertise in online video.

You can see more about our company at www.vantorell-example.tv and watch the video. The only thing you must keep is the logo (attached). Everything else is fair game.

We need the following sections:

Home
About Us
-Company
-Careers
-Management
Technology
-Publisher Solutions
-Advertiser Solutions
Press
Contact Us

On the main page should be a space where we can place our video plus showcase some important news such as whitepapers..etc.

Please include social media functions on the homepage such as twitter/facebook. Perhaps a section for a twitter feed.

Sites we like:
www.pelvagrin-example.com
www.quibbenlark-example.com
www.haskomelt-example.com
www.dorvanteq-example.com

Industry/Entity Type

Tv

Requirements
Nice to have
• social media feed

```html
<!DOCTYPE html>
<html lang="en">
<head>
<meta charset="utf-8">
<title>Vantorell — Online Video Media Technology</title>
<link rel="stylesheet" href="https://fonts.googleapis.com/css2?family=Quicksand:wght@400;500;700&family=Ubuntu:wght@400;700&family=Crimson+Text&family=Arimo&display=swap">
<style>
:root{
  --page:#efefef;
  --ink:#333333;
  --muted:#6b6b6b;
  --teal:#1f7f9c;
  --blue-top:#3596b8;
  --blue-bottom:#0b5673;
  --panel:#f8f8f8;
  --line:#e0e0e0;
  --video-card:#4f4843;
  --link:#1b5e96;
  --star:#f2d33a;
}
*{box-sizing:border-box;margin:0;padding:0}
html,body{width:1200px;height:1156px;overflow:hidden}
body{position:relative;background:var(--page);font-family:"Quicksand",sans-serif;color:var(--ink)}
.abs{position:absolute}
.band{background:linear-gradient(var(--blue-top),var(--blue-bottom));color:#fff}

/* header */
.brand{left:174px;top:22px;display:flex;align-items:center;gap:12px}
.brand-dot{width:40px;height:40px;border-radius:50%;background:var(--teal)}
.brand-name{font-family:"Quicksand",sans-serif;font-weight:500;font-size:50px;color:var(--teal);letter-spacing:1px;line-height:1}
.contact{right:177px;top:8px;text-align:right;font-style:italic;font-size:19px;line-height:27.5px;font-weight:500}

/* nav */
.nav-bar{left:0;top:97px;width:1200px;height:53px;border-top:1px solid #aaa;background:linear-gradient(#f9f9f9,#dcdcdc);box-shadow:0 3px 5px rgba(0,0,0,.25)}
.nav{left:174px;top:110px;display:flex;font-size:19px;gap:0}
.nav span{white-space:pre}
.nav .active{color:var(--teal)}
.social{left:850px;top:105px;display:flex;gap:11px}
.social i{display:block;width:35px;height:36px;border-radius:6px;background:linear-gradient(#a9a9a9,#6e6e6e);box-shadow:0 1px 2px rgba(0,0,0,.4)}

.dropdown{left:246px;top:150px;width:144px;height:91px;background:#e6e6e6;border:1px solid #aaa;box-shadow:1px 2px 3px rgba(0,0,0,.25);padding:4px 0 0 14px;font-size:19px;line-height:25px;color:#555;z-index:5}
.dropdown .current{color:var(--teal)}

/* panels */
.panel{background:var(--panel);border:1px solid var(--line)}
.side-head{left:184px;top:170px;width:287px;height:38px;font-size:19px;padding:8px 0 0 25px}
.side-list{left:184px;top:208px;width:287px;border:1px solid var(--line);background:#fafafa}
.side-list li{list-style:none;height:43px;border-bottom:1px solid var(--line);font-size:19px;padding:11px 0 0 25px;letter-spacing:.3px}

.deal{left:482px;top:170px;width:536px;height:256px;background:#f7f7f7;border:1px solid var(--line);overflow:hidden;font-family:"Ubuntu",sans-serif}
.deal h2{position:absolute;left:29px;top:32px;font-size:35px;font-weight:700;letter-spacing:.5px}
.deal .tick{position:absolute;left:177px;top:74px;font-family:"Quicksand",sans-serif;font-size:19px;font-weight:500}
.deal .miss{position:absolute;left:28px;top:105px;font-size:35px;font-weight:700;line-height:44px;letter-spacing:.5px}
.clock{position:absolute;left:352px;top:52px;width:146px;height:146px;border-radius:50%;background:radial-gradient(#ffffff 55%,#d8d8d8 62%,#8a8a8a 70%,#5e5e5e 100%)}
.ribbon{position:absolute;left:0;top:0}
.brochure{position:absolute;left:0;top:225px;width:536px;height:31px;font-size:18px;padding:4px 0 0 16px}
.dots{position:absolute;right:14px;top:232px;display:flex;gap:4px}
.dots i{width:16px;height:16px;border-radius:50%;background:#e9e9e9}

.player{left:184px;top:457px;width:432px;height:296px;border:1px solid #bbb;background:#fff}
.player-frame{position:absolute;left:0;top:0;width:430px;height:275px;background:linear-gradient(135deg,#e8e9ea,#c9ccd0 45%,#5a5e66 70%,#d6d7d9)}
.controls{position:absolute;left:0;top:275px;width:430px;height:19px;background:linear-gradient(#f2f2f2,#cfcfcf);font-family:"Arimo",sans-serif;font-size:9px}

.search{left:625px;top:457px;width:392px;height:30px}
.search-field{position:absolute;left:158px;top:3px;width:200px;height:24px;background:#fff;border:1px solid #ccc;font-family:"Crimson Text",serif;font-size:13px;color:#888;padding:3px 6px}
.search-btn{position:absolute;left:358px;top:3px;width:28px;height:24px;background:#3a3a3a}
.recent-title{left:627px;top:498px;font-family:"Crimson Text",serif;font-size:20px;letter-spacing:.5px}
.vid{left:626px;width:391px;height:69px;background:var(--video-card);color:#fff}
.vid .thumb{position:absolute;left:10px;top:8px;width:75px;height:53px;background:linear-gradient(135deg,#e9eaeb,#a9adb3 55%,#50545c);border:1px solid #ddd}
.vid h3{position:absolute;left:95px;top:3px;font-family:"Crimson Text",serif;font-weight:400;font-size:20px}
.vid p{position:absolute;left:95px;top:27px;font-family:"Arimo",sans-serif;font-size:11.5px;line-height:16px;letter-spacing:.2px}
.vid .stars{color:var(--star);letter-spacing:-1px;font-size:13px}
.vid .stars b{color:#fff;font-weight:400}

.article-head{left:177px;top:777px;width:848px;height:38px;font-family:"Crimson Text",serif;font-size:20px;padding:7px 0 0 30px;letter-spacing:.5px}
.article{left:177px;top:815px;width:848px;height:233px;background:#fbfbfb;border:1px solid var(--line);border-top:0}
.col{position:absolute;top:24px;font-family:"Arimo",sans-serif;font-size:11px;line-height:16.7px;color:var(--muted)}
.col .more{display:block;text-align:right;color:var(--link);margin-top:1px}
.divider{position:absolute;left:426px;top:22px;width:1px;height:195px;background:#ddd}

.to-top{left:1087px;top:941px;width:44px;height:46px;border-radius:10px;background:#d9d9d9;padding:3px}
.to-top div{width:38px;height:40px;border-radius:8px;background:linear-gradient(#5a5a5a,#1f1f1f)}

.footer{left:0;top:1062px;width:1200px;height:53px;border-top:1px solid #999;background:linear-gradient(#f5f5f5,#d6d6d6);box-shadow:0 3px 5px rgba(0,0,0,.2);text-align:center;font-family:"Arimo",sans-serif;font-size:11.5px;padding-top:10px;line-height:18px}
.footer .home{color:var(--link)}
</style>
</head>
<body>

<header>
  <div class="abs brand"><span class="brand-dot"></span><span class="brand-name">Vantorell</span></div>
  <address class="abs contact">+91 9400 555 018<br>info@vantorell-example.com<br>vantorell@mailbox-example.com</address>
</header>

<div class="abs nav-bar"></div>
<nav class="abs nav">
  <span>Home   |   </span><span class="active">About Us</span><span>   |   Technology   |   Press   |   Contact Us</span>
</nav>
<div class="abs social" aria-label="Social links"><i></i><i></i><i></i><i></i></div>

<ul class="abs dropdown">
  <li style="list-style:none" class="current">Company</li>
  <li style="list-style:none">Careers</li>
  <li style="list-style:none">Management</li>
</ul>

<main>
  <div class="abs panel" style="left:177px;top:163px;width:848px;height:273px"></div>
  <div class="abs side-head band">Whitepaper links</div>
  <ul class="abs side-list">
    <li>Loreum lipsum</li><li>Loreum lipsum</li><li>Loreum lipsum</li><li>Loreum lipsum</li><li style="border:0">Loreum lipsum</li>
  </ul>

  <section class="abs deal">
    <h2>Deal of the day</h2>
    <span class="tick">time’s ticking</span>
    <div class="miss">Don’t miss out<br>today’s one deal</div>
    <div class="clock" role="img" aria-label="Wall clock showing twelve o'clock"></div>
    <svg class="ribbon" width="536" height="100" viewBox="0 0 536 100">
      <polygon points="400,0 440,0 536,72 536,92" fill="#1f7f9c"/>
      <text x="0" y="0" transform="translate(452,22) rotate(37)" font-family="Crimson Text, serif" font-size="16" fill="#fff">Hurry up !</text>
    </svg>
    <div class="brochure band">Check Our New Brochure</div>
    <div class="dots"><i></i><i></i><i></i><i></i></div>
  </section>

  <div class="abs panel" style="left:177px;top:447px;width:848px;height:316px"></div>
  <div class="abs player">
    <div class="player-frame" role="img" aria-label="Business team meeting around a white round table, seen from above"></div>
    <div class="controls">
      <svg width="430" height="19" viewBox="0 0 430 19">
        <polygon points="9,4 20,9.5 9,15" fill="#222"/>
        <circle cx="37" cy="9.5" r="6" fill="#666"/>
        <rect x="44" y="7" width="264" height="5" rx="2" fill="#9a9a9a"/>
        <text x="323" y="13" font-family="Arimo, sans-serif" font-size="9" fill="#222">0:00 / 0:00</text>
        <polygon points="378,7 382,7 386,4 386,15 382,12 378,12" fill="#333"/>
        <rect x="406" y="4" width="18" height="11" fill="#333"/>
      </svg>
    </div>
  </div>

  <div class="abs search band">
    <div class="search-field">Search video's here...</div>
    <div class="search-btn">
      <svg width="28" height="24" viewBox="0 0 28 24"><circle cx="12.5" cy="10.5" r="5.5" fill="none" stroke="#fff" stroke-width="2.2"/><line x1="16.5" y1="14.5" x2="21" y2="19" stroke="#fff" stroke-width="2.6"/></svg>
    </div>
  </div>
  <div class="abs recent-title">Our recent video's</div>

  <div class="abs vid" style="top:537px"><div class="thumb" role="img" aria-label="Meeting video still"></div><h3>Lorem ipsum dolor</h3><p>consectetur adipiscing elit. Praesent at mauris<br>non nisi vestibulum facilisis &nbsp; 2:19 <span class="stars">★★★★★</span></p></div>
  <div class="abs vid" style="top:611px"><div class="thumb" role="img" aria-label="Meeting video still"></div><h3>Lorem ipsum dolor</h3><p>consectetur adipiscing elit. Praesent at mauris<br>non nisi vestibulum facilisis &nbsp; 2:19 <span class="stars">★★★★<b>★</b></span></p></div>
  <div class="abs vid" style="top:684px"><div class="thumb" role="img" aria-label="Meeting video still"></div><h3>Lorem ipsum dolor</h3><p>consectetur adipiscing elit. Praesent at mauris<br>non nisi vestibulum facilisis &nbsp; 2:19 <span class="stars">★★<b>★★★</b></span></p></div>

  <h2 class="abs article-head band" style="font-weight:400">Lorem ipsum dolor sit amet, consectetur adipiscing elit.</h2>
  <section class="abs article">
    <div class="col" style="left:30px;width:380px">Lorem ipsum dolor sit amet, consectetur adipiscing elit. Praesent at mauris non nisi vestibulum facilisis. Lorem ipsum dolor sit amet, consectetur adipiscing elit. Fusce mauris ligula, placerat nec euismod quis, facilisis sit amet ipsum. Ut et felis arcu, a pharetra velit. In metus orci, facilisis quis scelerisque et, tincidunt a lectus. Proin facilisis molestie posuere. Praesent erat tortor, dapibus quis ornare et, sodales non risus. Donec sit amet bibendum quam. Fusce porta enim at massa porttitor eget ultricies felis pharetra. In vestibulum, orci sed sagittis porta, odio nulla hendrerit dui, eget vehicula arcu sapien ut quam. In sed massa ac velit elementum placerat et ut neque.<span class="more">Read more...</span></div>
    <div class="divider"></div>
    <div class="col" style="left:451px;width:366px">Lorem ipsum dolor sit amet, consectetur adipiscing elit. Praesent at mauris non nisi vestibulum facilisis. Lorem ipsum dolor sit amet, consectetur adipiscing elit. Fusce mauris ligula, placerat nec euismod quis, facilisis sit amet ipsum. Ut et felis arcu, a pharetra velit. In metus orci, facilisis quis scelerisque et, tincidunt a lectus. Proin facilisis molestie posuere. Praesent erat tortor, dapibus quis ornare et, sodales non risus. Donec sit amet bibendum quam. Fusce porta enim at massa porttitor eget ultricies felis pharetra. In vestibulum, orci sed sagittis porta, odio nulla hendrerit dui, eget vehicula arcu sapien ut quam. In sed massa ac velit elementum placerat et ut neque.<span class="more" style="padding-right:10px">Read more...</span></div>
  </section>
</main>

<div class="abs to-top" aria-label="Back to top">
  <div><svg width="38" height="40" viewBox="0 0 38 40"><polygon points="19,7 33,21 25,21 25,33 13,33 13,21 5,21" fill="#fff"/></svg></div>
</div>

<footer class="abs footer">
  <div><span class="home">Home</span> &nbsp;| &nbsp;About Us &nbsp;| &nbsp;Technology &nbsp;| &nbsp;Press &nbsp;| &nbsp;Contact Us</div>
  <div>Copyright @ Vantorell &nbsp;| &nbsp;all right reserved</div>
</footer>

</body>
</html>
```